Consultant Firm Marketing Flyer

I want to use this flyer to market health care consultant services. I would like a front and back glossy, professional, yet bold and eye catching design. I would like it to convey knowledge, expertise, partnership and strength. The colors should blue and white but I am very open to the designer being creative. You can visit my website to see colors and images I want to use at brightharborcare.net
I would like the home page image on my website to be incorporated into the flyer but I am also open to other images that work with the design. The designer can be creative.

I want to highlight 4 service area’s of focus to my clients:
1. Revenue Cycle Optimization (making my clients money)
2. Practice Management Optimization (improving clinical operations)
3. Health Compliance (following the law)
4. Health Care Technology: (Telemedicine and AI)
Please be creative. Go where ever your creativity leads.

```html
<!DOCTYPE html>
<html lang="en">
<head>
<meta charset="utf-8">
<title>Bright Harbor Care – Consulting Flyer</title>
<link rel="stylesheet" href="https://fonts.googleapis.com/css2?family=Montserrat:wght@600;700&family=Open+Sans:wght@400;600&family=Raleway:wght@300&display=swap">
<style>
  :root{
    --navy:#1257a7;
    --sky:#2fa6d9;
    --ink:#4d4d4f;
    --grey:#c8c8c8;
    --paper:#ffffff;
    --photo-warm-a:#d9d4cf;
    --photo-warm-b:#b9a9a2;
    --photo-cool-a:#e6ecf1;
    --photo-cool-b:#b7c3cc;
  }
  *{box-sizing:border-box;margin:0;padding:0}
  html,body{width:1200px;height:734px;overflow:hidden;background:#fff}
  body{position:relative;font-family:"Open Sans",Arial,sans-serif;color:var(--ink)}

  .page{position:absolute;top:7px;width:546px;height:707px;background:var(--paper);
        box-shadow:6px 6px 10px rgba(0,0,0,.35);overflow:hidden}
  .page--front{left:18px}
  .page--back{left:634px}

  /* front */
  .hero-photo{position:absolute;left:0;top:0;width:546px;height:400px;
    background:linear-gradient(160deg,var(--photo-cool-a) 0%,var(--photo-warm-a) 45%,var(--photo-warm-b) 100%)}
  .hero-curve{position:absolute;left:0;top:350px}
  .brand{position:absolute;text-align:center;color:var(--navy);font-family:"Open Sans",Arial,sans-serif;
         font-weight:600;letter-spacing:.04em;white-space:nowrap}
  .brand__mark{display:inline-block;width:10px;height:10px;border-radius:50%;background:var(--navy);
               margin-right:6px;vertical-align:middle}
  .page--front .brand{left:0;width:546px;top:406px;font-size:16px}
  .section-title{position:absolute;left:0;width:546px;top:461px;text-align:center;
    font-family:Montserrat,Arial,sans-serif;font-weight:700;font-size:18px;color:var(--navy)}
  .section-rule{position:absolute;left:167px;top:487px;width:202px;height:1px;
    background:linear-gradient(90deg,transparent,var(--navy) 20%,var(--navy) 80%,transparent)}
  .bottom-band{position:absolute;left:0;bottom:0;width:546px;height:16px;background:var(--navy)}

  /* tags */
  .tag{position:absolute;width:180px;height:37px}
  .tag__shade,.tag__face{position:absolute;inset:0;clip-path:polygon(2% 0,100% 0,98% 100%,0 100%)}
  .tag__shade{transform:translate(5px,5px)}
  .tag__face{display:flex;align-items:center;justify-content:center;color:#fff;font-size:10.5px;white-space:nowrap}
  .tag--navy .tag__face{background:var(--navy)}
  .tag--sky .tag__face{background:var(--sky)}
  .tag--grey-shade .tag__shade{background:var(--grey)}
  .tag--navy-shade .tag__shade{background:var(--navy)}
  .tag--sky-shade .tag__shade{background:var(--sky)}

  /* back */
  .portrait{position:absolute;left:0;top:0}
  .tagline-disc{position:absolute;left:0;top:0}
  .tagline{position:absolute;left:283px;width:140px;top:142px;font-family:Raleway,Arial,sans-serif;font-weight:300;
           font-size:14px;letter-spacing:.28em;color:#fff;line-height:32px;white-space:nowrap}
  .page--back .brand{left:372px;width:175px;top:36px;font-size:10px}
  .service-copy{position:absolute;width:190px;font-size:10px;line-height:12.9px;color:var(--ink)}
  .social{position:absolute;top:620px;display:flex;gap:11px;left:226px}
  .social span{width:16px;height:16px;border-radius:50%;background:var(--navy)}
  .contact-band{position:absolute;left:0;top:640px;width:546px;height:67px;background:var(--navy);color:#fff;font-size:10.5px}
  .contact-band h3{position:absolute;left:0;width:522px;text-align:center;top:4px;
    font-family:Montserrat,Arial,sans-serif;font-weight:700;font-size:10.5px}
  .contact-line{position:absolute;display:flex;align-items:center;gap:8px;white-space:nowrap}
  .contact-line svg{flex:none}
</style>
</head>
<body>

<section class="page page--front">
  <div class="hero-photo" role="img" aria-label="Photo of four healthcare professionals meeting around a white table in a bright office"></div>
  <svg class="hero-curve" width="546" height="60" viewBox="0 0 546 60" aria-hidden="true">
    <path d="M0 42 Q273 -10 546 42 L546 60 L0 60 Z" fill="#fff"/>
    <path d="M0 42 Q273 -10 546 42 L546 50 Q273 6 0 50 Z" fill="var(--navy)"/>
  </svg>
  <div class="brand"><span class="brand__mark"></span>Bright Harbor Care LLC</div>
  <h2 class="section-title">OUR CORE SOLUTIONS</h2>
  <div class="section-rule"></div>

  <div class="tag tag--navy tag--grey-shade" style="left:27px;top:524px"><div class="tag__shade"></div><div class="tag__face">Revenue Cycle Optimization</div></div>
  <div class="tag tag--sky tag--grey-shade" style="left:273px;top:552px"><div class="tag__shade"></div><div class="tag__face">Practice Management Optimization</div></div>
  <div class="tag tag--sky tag--grey-shade" style="left:73px;top:607px"><div class="tag__shade"></div><div class="tag__face">Health Compliance</div></div>
  <div class="tag tag--navy tag--grey-shade" style="left:329px;top:630px"><div class="tag__shade"></div><div class="tag__face">Health Care Technology</div></div>

  <div class="bottom-band"></div>
</section>

<section class="page page--back">
  <svg class="portrait" width="546" height="320" viewBox="0 0 546 320">
    <defs>
      <linearGradient id="portraitTone" x1="0" y1="0" x2="1" y2="1">
        <stop offset="0" stop-color="var(--photo-cool-a)"/>
        <stop offset=".55" stop-color="#c9b3a5"/>
        <stop offset="1" stop-color="var(--photo-cool-b)"/>
      </linearGradient>
    </defs>
    <circle cx="118" cy="95" r="214" fill="url(#portraitTone)" role="img" aria-label="Photo of a smiling doctor in a white coat with colleagues behind her"/>
    <circle cx="118" cy="95" r="216" fill="none" stroke="var(--navy)" stroke-width="7"/>
  </svg>
  <svg class="tagline-disc" width="546" height="320" viewBox="0 0 546 320" aria-hidden="true">
    <circle cx="345" cy="195" r="93" fill="var(--navy)"/>
    <circle cx="352" cy="195" r="93" fill="var(--sky)"/>
  </svg>
  <p class="tagline">ADVANCING<br>HEALTHCARE<br>SOLUTIONS</p>
  <div class="brand"><span class="brand__mark"></span>Bright Harbor Care LLC</div>

  <div class="tag tag--sky tag--navy-shade" style="left:33px;top:312px"><div class="tag__shade"></div><div class="tag__face">Revenue Cycle Management</div></div>
  <div class="tag tag--navy tag--sky-shade" style="left:316px;top:304px"><div class="tag__shade"></div><div class="tag__face">Practice Management Optimization</div></div>
  <div class="tag tag--navy tag--sky-shade" style="left:31px;top:470px"><div class="tag__shade"></div><div class="tag__face">Health Compliance</div></div>
  <div class="tag tag--sky tag--navy-shade" style="left:311px;top:470px"><div class="tag__shade"></div><div class="tag__face">Health Care Technology</div></div>

  <p class="service-copy" style="left:32px;top:365px">In today’s increasingly complex health care environment it’s important now more than ever that medical practices. closely manage their revenue cycle. bright harbor care (bhc) understands the reimbursement land­scape</p>
  <p class="service-copy" style="left:313px;top:359px;width:205px">Practice Management is challenging and it requires the right balance of skill, knowledge, experience and management expertise. BHC Offers assessment and optimization in Patient Access &amp; Scheduling, Patient Experience,&nbsp; Staff Experience</p>
  <p class="service-copy" style="left:30px;top:527px;width:196px">Do you need Human Resources Manage­ment but don’t want the expense of a full service Human Resources Department? Not having a full service Human Resources Department can increase liability and be costly to your medical practice.</p>
  <p class="service-copy" style="left:313px;top:526px">Do you need Human Resources Manage­ment but don’t want the expense of a full service Human Resources Department? Not having a full service Human Resources Department can increase liability and be costly to your medical practice.</p>

  <div class="social" aria-label="Social links"><span></span><span></span><span></span></div>

  <footer class="contact-band">
    <h3>GET IN TOUCH</h3>
    <div class="contact-line" style="left:18px;top:18px">
      <svg width="8" height="12" viewBox="0 0 8 12"><rect x=".8" y=".8" width="6.4" height="10.4" rx="1.2" fill="none" stroke="#fff" stroke-width="1.4"/><circle cx="4" cy="9.3" r=".8" fill="#fff"/></svg>
      <span>(555) 014-2290</span>
    </div>
    <div class="contact-line" style="left:16px;top:37px">
      <svg width="12" height="8" viewBox="0 0 12 8"><rect width="12" height="8" fill="#fff"/><path d="M0 0 L6 4.5 L12 0" fill="none" stroke="var(--navy)" stroke-width="1"/></svg>
      <span>info@brightharborcare.net</span>
    </div>
    <div class="contact-line" style="left:328px;top:16px">
      <svg width="10" height="13" viewBox="0 0 10 13"><path d="M5 13 C5 13 0 7.5 0 5 A5 5 0 0 1 10 5 C10 7.5 5 13 5 13Z" fill="#fff"/><circle cx="5" cy="5" r="2" fill="var(--navy)"/></svg>
      <span>118 Harbor Ln, Newport, RI 02840, USA</span>
    </div>
    <div class="contact-line" style="left:328px;top:35px">
      <svg width="10" height="10" viewBox="0 0 10 10"><circle cx="5" cy="5" r="4.3" fill="none" stroke="#fff" stroke-width="1.2"/><path d="M.7 5 H9.3 M5 .7 C2.5 3 2.5 7 5 9.3 M5 .7 C7.5 3 7.5 7 5 9.3" fill="none" stroke="#fff" stroke-width=".9"/></svg>
      <span>www.brightharborcare.net</span>
    </div>
  </footer>
</section>

</body>
</html>
```